"Wellenhafen" private practice for physiotherapy

we are looking for a flyer design for a private practice for physiotherapy. the name of the practice is "Wellenhafen".
Treatments such as: manual therapy, manual lymphatic drainage, classic massage, sectoral alternative practitioners are offered

The flyers should be double-sided and the format DIN long (105x210 mm)

Font styles to use
Serif

Colors
0094D4
00A9DD
6FCCEA
C7EBF8
E9F6FB

Requirements
Must have
• Wellenhafen, Lindenweg 17, 04719 Mühlbach / Wellenhafen-praxis-beispiel.de / Tel. 03471 5820317

```html
<!DOCTYPE html>
<html lang="en">
<head>
<meta charset="utf-8">
<title>Wellenhafen – Physiotherapy Flyer</title>
<link rel="stylesheet" href="https://fonts.googleapis.com/css2?family=Poppins:wght@300;400;500;600;700;800;900&display=swap">
<style>
  :root {
    --stage: #e9eef2;
    --blue: #0a78c2;
    --blue-deep: #0b5fa3;
    --navy: #06132a;
    --cyan: #26d4e0;
    --sky: #9fdcf2;
    --ring: #1aa6cf;
    --white: #ffffff;
    --ink: #3a3f46;
    --light: #f2f4f6;
  }
  * { box-sizing: border-box; margin: 0; padding: 0; }
  html, body { width: 1200px; height: 800px; overflow: hidden; }
  body {
    background: var(--stage);
    font-family: "Poppins", sans-serif;
    position: relative;
  }
  .flyer {
    position: absolute;
    top: 40px;
    width: 360px;
    height: 720px;
    overflow: hidden;
    box-shadow: 0 10px 30px rgba(0,0,0,.18);
  }
  .flyer-front { left: 200px; background: var(--blue); }
  .flyer-back { left: 640px; background: var(--blue-deep); }
  .flyer svg.bg { position: absolute; inset: 0; }

  /* Front */
  .front-title {
    position: absolute; left: 28px; top: 62px;
    color: var(--white); font-weight: 800; font-size: 33px;
    letter-spacing: .5px;
  }
  .front-rule {
    position: absolute; left: 30px; top: 110px;
    width: 90px; height: 2px; background: var(--sky);
  }
  .front-subtitle {
    position: absolute; left: 30px; top: 116px;
    color: var(--sky); font-size: 20px; font-weight: 400;
  }
  .front-overlay-word {
    position: absolute; left: 34px; top: 318px;
    font-weight: 900; font-size: 36px; color: var(--ink);
    letter-spacing: .5px;
    transform: rotate(-4deg);
    transform-origin: left center;
  }
  .front-contact {
    position: absolute; left: 0; right: 0; bottom: 58px;
    text-align: center; color: var(--white); font-style: normal;
  }
  .front-contact .contact-name { font-weight: 600; font-size: 15px; margin-bottom: 4px; }
  .front-contact .contact-line { font-weight: 300; font-size: 13px; line-height: 1.4; }
  .front-contact .contact-phone { font-weight: 500; font-size: 13px; margin-top: 12px; }

  /* Back */
  .back-intro {
    position: absolute; left: 26px; right: 26px; top: 26px;
    color: var(--white); font-size: 13px; font-weight: 400;
    text-align: center; line-height: 1.3;
  }
  .back-heading {
    position: absolute; left: 0; right: 0; top: 146px;
    text-align: center; color: var(--cyan);
    font-size: 14px; font-weight: 500; line-height: 1.2;
  }
  .back-heading-rule {
    position: absolute; left: 115px; top: 186px;
    width: 135px; height: 2px; background: var(--white);
  }
  .service-list { position: absolute; left: 40px; top: 220px; list-style: none; }
  .service-item {
    display: flex; align-items: center; height: 56px; margin-bottom: 16px;
  }
  .service-icon {
    width: 54px; height: 54px; border-radius: 50%;
    background: var(--navy); flex: none; margin-right: 16px;
  }
  .service-label {
    color: var(--white); font-weight: 600; font-size: 14px; line-height: 1.2;
  }
  .booking {
    position: absolute; left: 0; right: 0; top: 560px; height: 60px;
    background: var(--light); text-align: center; color: var(--navy);
    padding-top: 6px;
  }
  .booking-label { font-size: 11px; font-weight: 500; letter-spacing: .3px; }
  .booking-phone {
    font-size: 26px; font-weight: 700; line-height: 1.2;
    display: inline-flex; align-items: center; gap: 6px;
  }
  .back-brand {
    position: absolute; left: 0; right: 0; bottom: 26px;
    text-align: center; color: var(--white);
    font-size: 30px; font-weight: 700;
  }
</style>
</head>
<body>

<section class="flyer flyer-front" aria-label="Flyer front">
  <svg class="bg" width="360" height="720" viewBox="0 0 360 720">
    <defs>
      <linearGradient id="photoTone" x1="0" y1="0" x2="1" y2="1">
        <stop offset="0" stop-color="#f3efe9"/>
        <stop offset=".45" stop-color="#e6a77c"/>
        <stop offset="1" stop-color="#d9d8d8"/>
      </linearGradient>
    </defs>
    <g role="img" aria-label="Photo of a therapist's hands massaging a patient's hand">
      <polygon points="0,215 360,90 360,430 0,560" fill="url(#photoTone)"/>
    </g>
    <circle cx="180" cy="330" r="140" fill="none" stroke="rgba(90,90,90,.35)" stroke-width="26"/>
    <circle cx="360" cy="130" r="50" fill="none" stroke="rgba(120,120,120,.3)" stroke-width="18"/>
    <circle cx="335" cy="500" r="40" fill="none" stroke="var(--ring)" stroke-width="16" opacity=".8"/>
    <circle cx="30" cy="690" r="55" fill="none" stroke="var(--ring)" stroke-width="18" opacity=".8"/>
  </svg>
  <h1 class="front-title">WELLENHAFEN</h1>
  <div class="front-rule"></div>
  <p class="front-subtitle">Physiotherapy</p>
  <p class="front-overlay-word">PHYSIOTHERAPY</p>
  <address class="front-contact">
    <p class="contact-name">Wellenhafen,</p>
    <p class="contact-line">Lindenweg 17,<br>04719 Mühlbach<br>Wellenhafen-praxis-beispiel.de</p>
    <p class="contact-phone">Tel. 03471 5820317</p>
  </address>
</section>

<section class="flyer flyer-back" aria-label="Flyer back">
  <svg class="bg" width="360" height="720" viewBox="0 0 360 720">
    <defs>
      <linearGradient id="backTone" x1="0" y1="0" x2="1" y2="1">
        <stop offset="0" stop-color="#0b5fa3"/>
        <stop offset=".6" stop-color="#1f7fc8"/>
        <stop offset="1" stop-color="#0b5fa3"/>
      </linearGradient>
    </defs>
    <rect x="0" y="0" width="360" height="125" fill="var(--navy)"/>
    <g role="img" aria-label="Photo of a woman stretching over an exercise ball, tinted blue">
      <rect x="0" y="125" width="360" height="435" fill="url(#backTone)"/>
    </g>
    <rect x="0" y="620" width="360" height="100" fill="var(--navy)"/>
  </svg>
  <p class="back-intro">Wellenhafen understand that you have individual needs and we will make your treatment plan so that it is specific to you.</p>
  <p class="back-heading">We offer specialist care<br>in the following area's;</p>
  <div class="back-heading-rule"></div>
  <ul class="service-list">
    <li class="service-item"><span class="service-icon" role="img" aria-label="Manual therapy icon"></span><span class="service-label">Manual Therapy</span></li>
    <li class="service-item"><span class="service-icon" role="img" aria-label="Lymphatic system icon"></span><span class="service-label">Manual Lymphatic<br>Drainage</span></li>
    <li class="service-item"><span class="service-icon" role="img" aria-label="Massage icon"></span><span class="service-label">Classic Massage</span></li>
    <li class="service-item"><span class="service-icon" role="img" aria-label="Caring hand icon"></span><span class="service-label">Sectoral Alternative<br>Practitioner</span></li>
  </ul>
  <div class="booking">
    <p class="booking-label">BOOK YOUR APPONTMENT TODAY ON</p>
    <p class="booking-phone">
      <svg width="20" height="20" viewBox="0 0 24 24" aria-hidden="true"><path fill="var(--navy)" d="M6.6 10.8a15.1 15.1 0 0 0 6.6 6.6l2.2-2.2a1 1 0 0 1 1-.25 11.4 11.4 0 0 0 3.6.57 1 1 0 0 1 1 1V20a1 1 0 0 1-1 1A17 17 0 0 1 3 4a1 1 0 0 1 1-1h3.5a1 1 0 0 1 1 1c0 1.25.2 2.45.57 3.57a1 1 0 0 1-.25 1z"/></svg>
      03471 5820317
    </p>
  </div>
  <p class="back-brand">Wellenhafen</p>
</section>

</body>
</html>
```